"Sketch Onward Club" Social Art Website Design

I need a design for a website I am building, which will be called Sketch Onward Club. I have attached the selected logo for the site. The site will be about drawing/art, and how art can be used to brighten a stranger's day as a random act of kindness. In real life, people will receive a drawing or piece of art with details for this site on it. They will in turn be able to give a drawing or piece of art to someone else, thus building a 'chain' of people who are related to each other through the drawings they have received. This should create a strong 'social' aspect to the site. There will be areas of the site for seeing other drawings/art that have been submitted, as well as for seeing different statistics (how many drawings have been submitted, where, how people are connected, etc.).

Target Market(s)

No specific target market.

Industry/Entity Type

Building

Coding

Number of Pages Required

1 page

Font styles to use
Sans Serif
Decorative

Requirements
Must have
• Must use the logo supplied.
Nice to have
• Should be colourful and artistic. References to art tools should be primarily around drawing, though painting can also feature. Colour scheme to match the logo would be ideal.

```html
<!DOCTYPE html>
<html lang="en">
<head>
<meta charset="utf-8">
<title>Sketch Onward Club</title>
<link href="https://fonts.googleapis.com/css2?family=Open+Sans:wght@400;600;700&family=Fredoka:wght@500;600&display=swap" rel="stylesheet">
<style>
:root{
  --pink:#f0237f;
  --pink-soft:#f9c3dc;
  --teal:#2db6c9;
  --ink:#3b3f47;
  --muted:#8a8f98;
  --hero-bg:#eef0f4;
  --white:#ffffff;
  --line:#e3e5ea;
  --foot:#f6f7f9;
}
*{box-sizing:border-box;margin:0;padding:0}
html,body{width:861px;height:1200px;overflow:hidden}
body{position:relative;font-family:"Open Sans",Arial,sans-serif;color:var(--ink);background:var(--white)}
.abs{position:absolute}

/* header */
.site-header{left:0;top:0;width:861px;height:36px;background:var(--white);box-shadow:0 1px 3px rgba(0,0,0,.08);z-index:2}
.brand{left:22px;top:10px;display:flex;align-items:center;gap:6px;font-family:"Fredoka",sans-serif;font-weight:600;font-size:11px;color:var(--pink)}
.brand-dot{width:16px;height:16px;border-radius:50%;background:var(--teal)}
.main-nav{left:322px;top:14px;display:flex;gap:17px;font-size:6.5px;font-weight:600;letter-spacing:.3px;text-transform:uppercase;color:var(--muted)}
.main-nav .active{color:var(--pink)}
.btn-signin{left:750px;top:9px;width:54px;height:17px;border-radius:2px;background:var(--teal);color:var(--white);font-size:6.5px;font-weight:700;text-align:center;line-height:17px;text-transform:uppercase}

/* hero */
.hero{left:0;top:36px;width:861px;height:294px;background:var(--hero-bg);overflow:hidden}
.hero-shape{left:0;top:0}
.hero-welcome{left:62px;top:108px;font-size:30px;font-weight:400;color:var(--ink)}
.hero-title{left:62px;top:146px;font-family:"Fredoka",sans-serif;font-weight:600;font-size:31px;color:var(--teal);letter-spacing:.5px}
.btn-outline{left:62px;top:212px;width:72px;height:18px;border:1px solid var(--pink);border-radius:2px;font-size:6.5px;color:var(--pink);text-align:center;line-height:16px}
.hero-art{left:470px;top:18px;width:340px;height:250px;border-radius:4px;
  background:
    radial-gradient(circle at 82% 18%,rgba(45,182,201,.35),transparent 28%),
    radial-gradient(circle at 72% 12%,rgba(240,35,127,.28),transparent 22%),
    radial-gradient(ellipse at 40% 45%,#ffffff 0 30%,transparent 46%),
    radial-gradient(ellipse at 30% 92%,rgba(45,182,201,.45),transparent 38%),
    radial-gradient(ellipse at 60% 60%,rgba(240,180,150,.35),transparent 40%),
    linear-gradient(160deg,#fbfbfd,#eef4f7)}
.hero-dots{left:62px;top:270px;display:flex;gap:4px}
.hero-dots span{width:4px;height:4px;border-radius:50%;background:var(--pink-soft)}
.hero-dots span:first-child{background:var(--pink)}

/* beliefs */
.beliefs{left:0;top:330px;width:861px;height:347px;background:var(--pink)}
.character{left:62px;top:66px;width:150px;height:250px;border-radius:70px 70px 30px 30px;
  background:
    radial-gradient(circle at 50% 22%,rgba(110,60,40,.55),transparent 32%),
    radial-gradient(ellipse at 50% 62%,rgba(247,160,60,.75),transparent 55%),
    linear-gradient(180deg,rgba(255,255,255,.22),rgba(255,255,255,.08))}
.beliefs h2{position:absolute;left:272px;font-size:14px;font-weight:700;color:var(--white)}
.beliefs p{position:absolute;left:272px;width:510px;font-size:8px;line-height:1.6;color:var(--white)}

/* artwork */
.artwork{left:0;top:677px;width:861px;height:266px;background:var(--white)}
.section-title{width:861px;text-align:center;font-size:15px;font-weight:600;color:var(--muted)}
.art-card{top:53px;width:225px;height:183px;background:var(--white);border:1px solid var(--line);box-shadow:0 2px 4px rgba(0,0,0,.06)}
.art-thumb{width:100%;height:94px}
.art-card h3{margin-top:18px;text-align:center;font-size:12px;font-weight:600;color:var(--ink)}
.art-card p{margin-top:3px;text-align:center;font-size:7px;color:var(--muted)}
.slide-label{font-size:7px;color:var(--muted)}

/* contact */
.contact{left:0;top:943px;width:861px;height:160px;background:var(--teal)}
.contact .section-title{color:var(--white);top:10px}
.contact-form{left:86px;top:40px;width:690px;height:100px;background:var(--white);border-radius:2px;padding:12px 14px}
.field-row{display:flex;gap:12px}
.field{flex:1;height:20px;border:1px solid var(--line);font-size:7px;color:var(--muted);line-height:18px;padding-left:8px}
.field.message{margin-top:10px;height:44px}
.btn-send{left:416px;top:148px;width:30px;height:30px;border-radius:50%;z-index:3}

/* footer */
.site-footer{left:0;top:1103px;width:861px;height:97px;background:var(--foot)}
.copyright{left:22px;top:64px;font-size:7px;color:var(--muted)}
.to-top{left:770px;top:60px;width:20px;height:20px}
</style>
</head>
<body>

<header class="site-header abs">
  <div class="brand abs"><span class="brand-dot"></span>Sketch Onward Club</div>
  <nav class="main-nav abs">
    <span class="active">Home</span><span>Idea &amp; Drawing</span><span>About</span><span>FAQ</span><span>Report</span><span>Our Policies</span><span>Contact</span>
  </nav>
  <div class="btn-signin abs">Sign In</div>
</header>

<section class="hero abs">
  <svg class="hero-shape abs" width="861" height="294" viewBox="0 0 861 294">
    <polygon points="610,0 861,0 861,294 360,294" fill="#ffffff"/>
  </svg>
  <div class="hero-art abs" role="img" aria-label="Illustration of a hand drawing a heart on paper with colourful pencils and markers around it"></div>
  <div class="hero-welcome abs">Welcome to</div>
  <div class="hero-title abs">Sketch Onward Club</div>
  <div class="btn-outline abs">View Artwork</div>
  <div class="hero-dots abs"><span></span><span></span><span></span></div>
  <svg class="abs" style="left:8px;top:215px" width="24" height="10" viewBox="0 0 24 10"><rect width="24" height="10" rx="2" fill="#f0237f"/><path d="M14 2 L9 5 L14 8" stroke="#fff" stroke-width="1.3" fill="none"/></svg>
  <svg class="abs" style="left:829px;top:215px" width="24" height="10" viewBox="0 0 24 10"><rect width="24" height="10" rx="2" fill="#f0237f"/><path d="M10 2 L15 5 L10 8" stroke="#fff" stroke-width="1.3" fill="none"/></svg>
</section>

<section class="beliefs abs">
  <div class="character abs" role="img" aria-label="Cartoon illustration of a young artist holding a paint palette and brush"></div>
  <h2 style="top:68px">What we Believe</h2>
  <p style="top:92px">"We believe that the gift of hand-made art, a simple drawing with a kind message, can brighten a stranger's day and make the world feel a little friendlier. We also believe everyone is an artist, whether or not you have ever held a brush, and that small acts can grow into a long chain of kindness passed from one person to the next."</p>
  <h2 style="top:186px">About us</h2>
  <p style="top:210px">Sketch Onward Club is a place where drawings travel from hand to hand. Each piece carries a note inviting the person who receives it to make a new one and pass it on. Here you can follow the chain, see the art people share, check where drawings have travelled and discover how far one small sketch can go.</p>
</section>

<section class="artwork abs">
  <div class="section-title abs" style="top:18px">Recently Submitted Artwork</div>
  <div class="slide-label abs" style="left:22px;top:140px">&#8249; Prev</div>
  <div class="slide-label abs" style="left:815px;top:140px">Next &#8250;</div>
  <article class="art-card abs" style="left:63px">
    <div class="art-thumb" role="img" aria-label="Painting of a sunset with a silhouetted tree" style="background:linear-gradient(180deg,#f7a21b,#d8431a 60%,#3a1a10)"></div>
    <h3>Art Title</h3><p>By Artist Name</p>
  </article>
  <article class="art-card abs" style="left:318px">
    <div class="art-thumb" role="img" aria-label="Painting of seagulls over ocean waves" style="background:linear-gradient(180deg,#2f6fb5,#7cb7dc 55%,#c9a77a)"></div>
    <h3>Art Title</h3><p>By Artist Name</p>
  </article>
  <article class="art-card abs" style="left:573px">
    <div class="art-thumb" role="img" aria-label="Painting of a lighthouse on a rocky shore" style="background:linear-gradient(180deg,#e9a86a,#c1613f 55%,#5b4a3a)"></div>
    <h3>Art Title</h3><p>By Artist Name</p>
  </article>
</section>

<section class="contact abs">
  <div class="section-title abs">Contact us</div>
  <form class="contact-form abs">
    <div class="field-row">
      <div class="field">Full Name</div>
      <div class="field">Email Address</div>
      <div class="field">Subject or Phone</div>
    </div>
    <div class="field message">Type your message here...</div>
  </form>
  <svg class="btn-send abs" viewBox="0 0 30 30"><circle cx="15" cy="15" r="14" fill="#2db6c9" stroke="#fff" stroke-width="2"/><path d="M9 15 L21 9 L17 21 L15 16 Z" fill="#fff"/></svg>
</section>

<footer class="site-footer abs">
  <div class="copyright abs">© 2024 Sketch Onward Club</div>
  <svg class="to-top abs" viewBox="0 0 20 20"><circle cx="10" cy="10" r="10" fill="#f0237f"/><path d="M6 12 L10 8 L14 12" stroke="#fff" stroke-width="1.5" fill="none"/></svg>
</footer>

</body>
</html>
```